Website for Prestigious Trailers and Floats

Design a prestigious website, to be used on mobile phones, and computers.
Must be able to be edited by myself
Please refer to www.marwickhaulage.com.au
Needs to focus on the "Marwick Haulage"" name, and the "Dunmore Parkes Towing" name.
Three trailer types to be highlighted are KR724/KR719 Horse Floats, PL3087 /PL62 Trailers, and VM8254/5942 Tipper Trailers
Needs Home Page,
Home page to include highlighted trailer types, slider for testimonials, Phone number, location, social media links, blog/news spot
Page for each of the highlighted trailer types/variations on the model
Page for multiple other trailer types

Logo's attached, can be broken up and used in parts if necessary for design

Target Market(s)

Western Australia, Horse People, Commercial Trailer Users, Handymen, Mini Digger Users, Tradesmen

Industry/Entity Type

Mining, Commercial, Government, Trades, Industry, Hobbyist

Coding

Coded - Design and coding required

Number of Pages Required

5+ page

Requirements
Must have
• See brief above
Nice to have
• See brief above

```html
<!DOCTYPE html>
<html lang="en">
<head>
<meta charset="utf-8">
<title>Marwick Haulage</title>
<link href="https://fonts.googleapis.com/css2?family=Poppins:wght@400;500;600;700&display=swap" rel="stylesheet">
<style>
:root{
  --orange:#e2562b;
  --blue:#0d3f94;
  --blue-deep:#0a2f75;
  --ink:#1f1f1f;
  --muted:#555;
  --grey-card:#7c8590;
  --footer:#1b1d22;
  --white:#fff;
  --peach:#f3c9b8;
  --star:#f5b400;
}
*{box-sizing:border-box;margin:0;padding:0}
html,body{width:1200px;height:2916px;overflow:hidden}
body{font-family:"Poppins",sans-serif;color:var(--ink);background:var(--white);position:relative}
a{color:inherit;text-decoration:none}

.topnav{height:72px;display:flex;align-items:center;justify-content:flex-end;padding-right:90px;gap:34px;font-size:15px;font-weight:500}
.topnav .icons{display:flex;gap:12px;margin-left:10px}
.topnav .icons span{width:26px;height:26px;border-radius:50%;background:var(--ink);display:block}
.topnav .icons span+span{background:none;border:2px solid var(--orange)}

.brandbar{position:absolute;top:104px;left:0;width:1200px;height:72px}
.brand{position:absolute;left:112px;top:6px;width:372px;height:56px;background:var(--orange);display:flex;align-items:center;justify-content:center;color:var(--white);font-weight:700;font-size:26px;letter-spacing:1px}
.search{position:absolute;left:680px;top:16px;width:210px;height:40px;border:1px solid #999;border-radius:20px;display:flex;align-items:center;padding-left:16px;font-size:14px;color:#444}
.search .btn{position:absolute;right:3px;top:3px;width:32px;height:32px;border-radius:50%;background:var(--ink)}
.call{position:absolute;left:910px;top:20px;display:flex;align-items:center;gap:10px;font-size:17px;font-weight:500}
.call b{font-weight:700}
.call .ph{width:32px;height:32px;border-radius:50%;background:var(--orange);display:flex;align-items:center;justify-content:center}

.hero{position:absolute;top:192px;left:0;width:1200px;height:488px;overflow:hidden}
.hero-photo{position:absolute;inset:0;background:
  radial-gradient(ellipse 280px 200px at 860px 250px,rgba(226,86,43,.55),rgba(226,86,43,0) 70%),
  radial-gradient(ellipse 420px 170px at 820px 300px,rgba(40,44,50,.55),rgba(40,44,50,0) 75%),
  linear-gradient(180deg,#c9dceb 0%,#e4edf3 28%,#7f9a6a 40%,#5f7a52 50%,#9aa0a6 58%,#6e747b 80%,#565c63 100%)}
.hero-text{position:absolute;left:100px;top:200px;width:370px}
.hero-text h1{font-size:26px;line-height:1.38;font-weight:700;color:var(--white);background:rgba(0,0,0,.6);padding:10px 12px}
.hero-text p{color:var(--white);font-size:15px;margin:10px 0 0 12px}
.btn-sales{display:inline-block;margin:18px 0 0 12px;background:var(--orange);color:var(--white);font-size:15px;font-weight:500;padding:8px 24px}

.categories{position:absolute;top:680px;left:0;width:1200px;height:540px;background:linear-gradient(180deg,#eceef0 0%,#f1dcd3 60%,var(--peach) 100%)}
.section-title{text-align:center;font-size:34px;font-weight:700;letter-spacing:1px}
.categories .section-title{color:var(--orange);margin-top:96px}
.cat{position:absolute;top:176px;width:310px;text-align:center}
.cat .photo{width:300px;height:236px;margin:0 auto;border-radius:50%;border:6px solid var(--white);box-shadow:0 2px 8px rgba(0,0,0,.15)}
.cat .photo.floats{background:radial-gradient(ellipse 70px 50px at 55% 58%,#e06a2c,rgba(224,106,44,0) 80%),linear-gradient(180deg,#d7e3ea 0%,#cfdae0 30%,#8b8f90 55%,#b7b0a6 75%,#9c968d 100%)}
.cat .photo.general{background:radial-gradient(ellipse 80px 60px at 50% 50%,#d2442a,rgba(210,68,42,0) 80%),linear-gradient(180deg,#e6ecef 0%,#c8cfd2 35%,#6c7276 60%,#3f4448 100%)}
.cat .photo.tipper{background:radial-gradient(ellipse 70px 55px at 50% 45%,#2f6a34,rgba(47,106,52,0) 80%),linear-gradient(180deg,#cfe0ea 0%,#a9c49a 35%,#6f8e5c 55%,#8d9196 75%,#666b70 100%)}
.cat .pill{position:absolute;top:260px;left:5px;width:300px;height:46px;border:3px solid var(--orange);border-radius:24px;background:var(--white);display:flex;align-items:center;justify-content:center;font-size:13px;font-weight:600;box-shadow:0 0 0 5px #f7d5c7}

.blog{position:absolute;top:1248px;left:0;width:1200px;height:624px;background:radial-gradient(circle at 50% 40%,#1c5bc4 0%,var(--blue) 55%,var(--blue-deep) 100%)}
.blog .section-title{color:var(--white);margin-top:100px}
.post{position:absolute;top:200px;width:480px;height:272px;background:var(--white);display:flex;padding:16px;gap:18px}
.post .thumb{flex:0 0 190px;height:176px}
.post .thumb.meeting{background:radial-gradient(ellipse 60px 70px at 30% 55%,#3d4f6a,rgba(61,79,106,0) 80%),linear-gradient(160deg,#d9dde2 0%,#aeb6bf 45%,#6b7683 100%)}
.post .thumb.workshop{background:radial-gradient(ellipse 60px 80px at 55% 60%,#c88a3a,rgba(200,138,58,0) 80%),linear-gradient(160deg,#e2ddd4 0%,#b9b1a3 50%,#7d7468 100%)}
.post .meta{position:absolute;left:16px;top:212px;width:190px;display:flex;align-items:center;gap:10px;font-size:13px;font-weight:600}
.post .meta i{width:18px;height:18px;border:2px solid var(--ink);border-radius:3px;display:block}
.post h3{font-size:18px;font-weight:600;margin-bottom:6px}
.post p{font-size:13px;line-height:1.7;color:var(--muted)}
.dots{position:absolute;left:0;width:1200px;display:flex;justify-content:center;gap:10px}
.dots span{width:14px;height:14px;border-radius:50%;border:2px solid #bbb;display:block}
.blog .dots span{background:var(--white);border-color:var(--white)}
.blog .dots span:first-child{opacity:.5}

.testimonials{position:absolute;top:1872px;left:0;width:1200px;height:620px}
.testimonials .section-title{color:var(--orange);margin-top:104px}
.quote{position:absolute;background:var(--grey-card);color:var(--white);text-align:center;padding:30px 24px 0}
.quote .mark{font-size:70px;line-height:.7;font-weight:700;opacity:.6;height:44px}
.quote p{font-size:14px;line-height:1.5}
.quote .stars{color:var(--star);font-size:22px;letter-spacing:6px;margin-top:14px}
.quote .avatar{position:absolute;left:50%;bottom:-40px;margin-left:-36px;width:72px;height:72px;border-radius:50%;border:4px solid var(--white);background:linear-gradient(135deg,#d9c2b0,#8a6f5c)}
.quote.side{top:216px;width:296px;height:212px}
.quote.main{top:192px;left:432px;width:336px;height:264px;background:var(--blue);padding-top:40px}
.quote.main p{font-size:17px}
.testimonials .dots{top:544px}
.testimonials .dots span:nth-child(3){background:#555;border-color:#555}

.footer{position:absolute;top:2492px;left:0;width:1200px;height:424px;background:var(--footer);color:var(--white)}
.foot-brand{position:absolute;left:120px;top:92px;width:170px;height:62px;background:var(--blue);display:flex;align-items:center;justify-content:center;font-size:13px;font-weight:600;text-align:center;line-height:1.2}
.social{position:absolute;left:120px;top:200px;display:flex;gap:14px}
.social span{width:34px;height:34px;border-radius:50%;background:var(--blue);display:block}
.social span:nth-child(2){background:var(--orange)}
.social span:nth-child(3){background:#444}
.col{position:absolute;top:80px;font-size:14px}
.col h4{font-size:15px;font-weight:600;margin-bottom:26px}
.col li{list-style:none;margin-bottom:12px;color:#ddd}
.contact li{display:flex;gap:12px;align-items:flex-start;line-height:1.5}
.contact .ic{flex:0 0 22px;height:22px;border-radius:50%;border:2px solid #ddd;margin-top:2px}
.copy{position:absolute;top:368px;width:1200px;text-align:center;font-size:13px;color:#ccc}
</style>
</head>
<body>

<nav class="topnav">
  <a href="#">HOME</a><a href="#">HIRE</a><a href="#">TRAILERS</a><a href="#">HORSE FLOATS</a><a href="#">NEWS</a><a href="#">MANUALS</a><a href="#">CONTACT</a>
  <div class="icons"><span></span><span></span><span></span></div>
</nav>

<div class="brandbar">
  <div class="brand">MARWICK HAULAGE</div>
  <div class="search">Search Products<span class="btn"></span></div>
  <div class="call">CALL <b>0400 386 142</b>
    <span class="ph"><svg width="16" height="16" viewBox="0 0 24 24"><path fill="#fff" d="M6.6 10.8a15 15 0 006.6 6.6l2.2-2.2a1 1 0 011-.25 11.4 11.4 0 003.6.57 1 1 0 011 1V20a1 1 0 01-1 1A17 17 0 013 4a1 1 0 011-1h3.5a1 1 0 011 1c0 1.25.2 2.45.57 3.6a1 1 0 01-.25 1z"/></svg></span>
  </div>
</div>

<section class="hero">
  <div class="hero-photo" role="img" aria-label="Tracked loader carried on a heavy plant trailer along an open country road"></div>
  <div class="hero-text">
    <h1>Built in Wales UK... Engineered to the highest standards... Surviving the toughest outback!</h1>
    <p>Trailers to cast...</p>
    <a class="btn-sales" href="#">SALES</a>
  </div>
</section>

<section class="categories">
  <h2 class="section-title">CATEGORIES</h2>
  <div class="cat" style="left:107px"><div class="photo floats" role="img" aria-label="Horse float trailer carrying an orange mini digger"></div><div class="pill">KR724/KR719 HORSE FLOATS</div></div>
  <div class="cat" style="left:445px"><div class="photo general" role="img" aria-label="Red site dumper loaded on a general purpose trailer"></div><div class="pill">PL3087 /PL62 TRAILERS</div></div>
  <div class="cat" style="left:781px"><div class="photo tipper" role="img" aria-label="Green ride-on machine on a tipper trailer"></div><div class="pill">VM8254/5942 TIPPER TRAILERS</div></div>
</section>

<section class="blog">
  <h2 class="section-title">OUR BLOG</h2>
  <article class="post" style="left:112px">
    <div class="thumb meeting" role="img" aria-label="Team meeting around an office table"></div>
    <div class="meta"><i></i>04-OCT-2022</div>
    <div><h3>Lorem Ipsum</h3><p>Lorem ipsum dolor sit amet, consectetur adipiscing elit, sed do eiusmod tempor incididunt ut labore et dolore magna aliqua. Quis ipsum suspendisse ultrices gravida. Risus commodo viverra maecenas.</p></div>
  </article>
  <article class="post" style="left:608px">
    <div class="thumb workshop" role="img" aria-label="Staff member in a trailer workshop"></div>
    <div class="meta"><i></i>07-OCT-2022</div>
    <div><h3>Lorem Ipsum</h3><p>Lorem ipsum dolor sit amet, consectetur adipiscing elit, sed do eiusmod tempor incididunt ut labore et dolore magna aliqua. Quis ipsum suspendisse ultrices gravida. Risus commodo viverra maecenas.</p></div>
  </article>
  <div class="dots" style="top:540px"><span></span><span></span></div>
</section>

<section class="testimonials">
  <h2 class="section-title">TESTIMONIALS</h2>
  <div class="quote side" style="left:112px"><div class="mark">&ldquo;</div><p>Lorem ipsum dolor sit amet, consectetur adipiscing elit, sed do eiusmod tempor incididunt ut</p><div class="stars">★★★★★</div><div class="avatar" role="img" aria-label="Customer portrait"></div></div>
  <div class="quote main"><div class="mark">&ldquo;</div><p>Lorem ipsum dolor sit amet, consectetur adipiscing elit, sed do eiusmod tempor incididunt ut</p><div class="stars">★★★★★</div><div class="avatar" role="img" aria-label="Customer portrait"></div></div>
  <div class="quote side" style="left:792px"><div class="mark">&ldquo;</div><p>Lorem ipsum dolor sit amet, consectetur adipiscing elit, sed do eiusmod tempor incididunt ut</p><div class="stars">★★★★★</div><div class="avatar" role="img" aria-label="Customer portrait"></div></div>
  <div class="dots"><span></span><span></span><span></span><span></span></div>
</section>

<footer class="footer">
  <div class="foot-brand">Dunmore Parkes<br>Towing</div>
  <div class="social"><span></span><span></span><span></span></div>
  <div class="col" style="left:396px"><h4>Quick Links</h4><ul><li>Home</li><li>About Us</li><li>Our Team</li><li>Services</li><li>Ledger Client Login</li></ul></div>
  <div class="col" style="left:628px"><h4>Help Links</h4><ul><li>Privacy Policy</li><li>Terms of Agreement</li></ul></div>
  <div class="col contact" style="left:868px"><h4>Contact Us</h4><ul>
    <li><span class="ic"></span><span>3/88 Ranford Rd, 88 Ranford Rd<br>Kenwick WA<br>6107, Australia</span></li>
    <li><span class="ic"></span><span>0400 386 142</span></li></ul></div>
  <div class="copy">Copyright @2023 Marwickhaulage All Right Reserved.</div>
</footer>

</body>
</html>
```